New corporate powerpoint template

We need a fresh new look to update our powerpoint tempalte

Target Market(s)

Large Manufacturing corporations in the Automotive, Aerospace & Defense and Medical Device indutries

Requirements
Should not have
• Need to maximize slide area for content.

```html
<!DOCTYPE html>
<html lang="en">
<head>
<meta charset="UTF-8">
<title>Veranta – Title Slide</title>
<link href="https://fonts.googleapis.com/css2?family=Mulish:wght@400;600;800&display=swap" rel="stylesheet">
<style>
  :root {
    --violet-deep: #3a1a6e;
    --violet: #7a3fb0;
    --lilac: #c9a6e0;
    --glow: #f1e9fa;
    --navy: #1d2d6a;
    --teal: #3b7c93;
    --brand-blue: #356d8c;
    --gold: #c59a2c;
    --white: #ffffff;
  }
  * { margin: 0; padding: 0; box-sizing: border-box; }
  html, body {
    width: 1200px;
    height: 900px;
    overflow: hidden;
    background: var(--white);
  }
  .slide {
    position: relative;
    width: 1200px;
    height: 900px;
    overflow: hidden;
    font-family: "Mulish", "Helvetica Neue", Arial, sans-serif;
  }
  .backdrop {
    position: absolute;
    inset: 0;
    background:
      radial-gradient(ellipse 320px 420px at 430px 300px, var(--glow) 0%, rgba(225,200,240,0.7) 35%, rgba(160,100,200,0) 75%),
      radial-gradient(ellipse 500px 360px at 900px 140px, rgba(190,150,220,0.8) 0%, rgba(120,60,170,0) 70%),
      radial-gradient(ellipse 520px 380px at 120px 160px, rgba(40,60,140,0.9) 0%, rgba(40,60,140,0) 70%),
      radial-gradient(ellipse 600px 300px at 300px 760px, rgba(70,20,110,0.9) 0%, rgba(70,20,110,0) 70%),
      linear-gradient(135deg, var(--navy) 0%, var(--violet) 45%, var(--violet-deep) 100%);
  }
  .brand-panel {
    position: absolute;
    left: 758px;
    top: 312px;
    width: 442px;
    height: 267px;
    background: var(--white);
    box-shadow: -4px 4px 14px rgba(30,10,60,0.35);
    display: flex;
    flex-direction: column;
    align-items: center;
    justify-content: center;
    padding-left: 30px;
  }
  .brand-name {
    font-size: 64px;
    font-weight: 600;
    color: var(--brand-blue);
    letter-spacing: 2px;
    line-height: 1;
    margin-bottom: 30px;
  }
  .brand-descriptor {
    font-size: 20px;
    font-weight: 600;
    color: var(--brand-blue);
    letter-spacing: 0.5px;
  }
  .brand-slogan {
    font-size: 20px;
    font-weight: 400;
    color: var(--brand-blue);
    margin-top: 6px;
  }
  .accent-rule {
    position: absolute;
    left: 0;
    top: 828px;
    width: 100%;
    height: 7px;
    background: var(--teal);
  }
  .value-band {
    position: absolute;
    left: 0;
    top: 835px;
    width: 100%;
    height: 65px;
    background: var(--gold);
    display: flex;
    align-items: center;
    justify-content: center;
    padding-right: 130px;
  }
  .value-statement {
    color: var(--white);
    font-size: 26px;
    font-weight: 800;
    letter-spacing: 0.3px;
  }
</style>
</head>
<body>
  <main class="slide">
    <div class="backdrop" role="img" aria-label="Abstract glowing violet and blue light-swirl background"></div>

    <section class="brand-panel">
      <div class="brand-name">Veranta</div>
      <div class="brand-descriptor">Quality &amp; Compliance Software</div>
      <div class="brand-slogan">Right the First Time</div>
    </section>

    <div class="accent-rule"></div>
    <footer class="value-band">
      <p class="value-statement">Proven / Flexible / Scalable / A Quality Performance Driven Solution</p>
    </footer>
  </main>
</body>
</html>
```